Visitenkarten für Mentorin für Frauen
Zielgruppe
Ich bin Mentorin für Frauen (30-50 Jahre alt), die ihre Berufung endlich finden möchten und sich nach mehr Energie und Sinn sehnen. Ich helfe ihnen mit meiner (Name fehtl noch)-Methode ihren Seelenweg zu finden und zu gehen, sodass sie vor Energie übersprudeln und mit einem Leuchten in den Augen ein Leben in Fluss und Fülle kreieren.
Sie sind nicht unglücklich, aber es fehtl ihnen was, das sie wirklich erfüllt.
Stichwörter: Numerologie, Human Design, Seelenweg, Berufung, Lebensaufgabe, erfüllt sein- endlich die Leere füllen, Freiheit, Selbstbestimmt, Selbstliebe, Potentialentfaltung, Transformation
meine core story:
Mit Freude, unglaublicher Energie und einem Strahlen in den Augen schon vor dem Wecker aufzustehen, war für mich früher undenkbar. Ich konnte mir nicht vorstellen, wie sich Leute auf den Montag freuen konnten.
Dabei hätte mich nicht als unglücklich bezeichnet, aber es fehlt einfach etwas, ich hatte eine innere Leere und eine Sehnsucht nach dem Sinn in meinem Lebe, wollte so geliebt werden wie ich bin und mich auch so zeigen können. Ich weiß wie es ist sich klein, unsicher zu fühlen und nicht zu wissen woher das kommt. Ich habe es einfach nicht für möglich gehalten, dass diese innere Leere so leicht zu füllen ist und Freude, Spaß, Selbstbewusstseein und Leichtigkeit in allen Bereichen mit sich bringt.
Weil ich selbst diesen Weg gegangen bin und weil ich weiß, dass es nichts erfüllenderes gibt als das schlummernde Potential zu erwecken, begleite ich Frauen dabei ihren Seelenweg zu finden und zu gehen.
Dadurch dass sie genau wissen, was ihre Gaben sind und was ihre Seele glücklich macht, haben sie Spaß und Freude, gerade auch in den alltäglichen Dingen. Sie führen ein selbstbestimmtes Leben, lieben sich selbst und zeigen sich so wie sie sind.Die gigantische Energie die dadurch in ihnen frei wird, lässt sie die bisherigen Grenzen überwinden. Sie tun was sie erfüllt, o..
Aufgabenstellung
weiblich, geschwungen, weich: beinhalten solls:
Helena Wortmann
Mentorin für Powerfrauen
(Lebe deine Berufung)--> da bin ich mir nicht ganz sicher ob das gut aussehn wird oder zuviel wird
falls relevant habe ich bisher folgende Schriftarten verwendet: Canva Sans und Tan mon cheri
ist aber kein muss

```html
<!DOCTYPE html>
<html lang="de">
<head>
<meta charset="utf-8">
<title>Helena Wortmann – Visitenkarten</title>
<link href="https://fonts.googleapis.com/css2?family=Gilda+Display&family=Cormorant+Garamond:wght@400;500&display=swap" rel="stylesheet">
<style>
  :root {
    --bg: #e8cbbd;
    --peach: #eeb98c;
    --apricot: #f0c27e;
    --rose: #e49a9a;
    --blush: #e9a6a0;
    --ink: #fff7f0;
    --ink-soft: rgba(255, 247, 240, 0.88);
    --shadow: rgba(120, 70, 50, 0.18);
  }
  * { box-sizing: border-box; margin: 0; padding: 0; }
  html, body {
    width: 1200px; height: 800px; overflow: hidden;
    background: var(--bg);
  }
  .sheet {
    width: 1200px; height: 800px;
    display: flex; align-items: center; justify-content: center; gap: 48px;
  }
  .card {
    position: relative;
    width: 520px; height: 320px;
    border-radius: 4px;
    color: var(--ink);
    box-shadow: 0 14px 36px var(--shadow);
    overflow: hidden;
  }
  .card--back {
    background:
      radial-gradient(ellipse at 85% 80%, var(--apricot) 0%, transparent 55%),
      linear-gradient(150deg, var(--blush) 0%, var(--peach) 60%, var(--apricot) 100%);
  }
  .card--front {
    background:
      radial-gradient(ellipse at 15% 45%, var(--apricot) 0%, transparent 55%),
      linear-gradient(120deg, var(--peach) 0%, var(--peach) 45%, var(--rose) 100%);
  }
  .name {
    font-family: "Gilda Display", "Cormorant Garamond", serif;
    font-weight: 400;
    letter-spacing: 0.5px;
    color: var(--ink);
  }
  .role, .tagline, .contact {
    font-family: "Cormorant Garamond", serif;
    color: var(--ink-soft);
  }
  /* back side */
  .card--back .identity {
    position: absolute; top: 74px; left: 150px; right: 30px;
    text-align: center;
  }
  .card--back .name { font-size: 38px; line-height: 1; }
  .card--back .role { font-size: 21px; margin-top: 8px; letter-spacing: 0.3px; }
  .contact { font-size: 14px; line-height: 1.55; }
  .contact-list {
    position: absolute; left: 34px; bottom: 92px;
    list-style: none;
  }
  .contact-list li { display: flex; align-items: center; gap: 10px; }
  .contact-list svg, .address svg { width: 13px; height: 13px; flex: none; }
  .address {
    position: absolute; right: 60px; bottom: 34px;
    display: flex; gap: 10px; align-items: flex-start;
  }
  .address svg { margin-top: 3px; }
  /* front side */
  .card--front .brand {
    position: absolute; top: 118px; left: 0; right: 0;
    display: flex; align-items: center; justify-content: center; gap: 14px;
  }
  .brand-dot {
    width: 12px; height: 12px; border-radius: 50%;
    border: 1.4px solid var(--ink);
  }
  .card--front .name { font-size: 40px; }
  .card--front .tagline {
    position: absolute; bottom: 58px; left: 0; right: 0;
    text-align: center; font-size: 18px; letter-spacing: 0.6px;
  }
</style>
</head>
<body>
<main class="sheet">
  <section class="card card--back" aria-label="Rückseite mit Kontaktdaten">
    <div class="identity">
      <h1 class="name">Helena Wortmann</h1>
      <p class="role">Mentorin für Powerfrauen</p>
    </div>
    <ul class="contact contact-list">
      <li>
        <svg viewBox="0 0 16 16" fill="none" stroke="currentColor" stroke-width="1.3"><path d="M4 1.5l2 3-1.5 1.5a8 8 0 0 0 5.5 5.5L11.5 10l3 2-1.5 2.5C7 14.5 1.5 9 1.5 3z"/></svg>
        <span>+43 (0) 000 / 000 00 00</span>
      </li>
      <li>
        <svg viewBox="0 0 16 16" fill="none" stroke="currentColor" stroke-width="1.3"><rect x="1.5" y="3.5" width="13" height="9"/><path d="M1.5 3.5l6.5 5 6.5-5"/></svg>
        <span>hallo@wortmann-weg.de</span>
      </li>
      <li>
        <svg viewBox="0 0 16 16" fill="none" stroke="currentColor" stroke-width="1.3"><circle cx="8" cy="8" r="6.5"/><ellipse cx="8" cy="8" rx="2.8" ry="6.5"/><path d="M1.5 8h13"/></svg>
        <span>www.wortmann-weg.de</span>
      </li>
    </ul>
    <div class="contact address">
      <svg viewBox="0 0 16 16" fill="none" stroke="currentColor" stroke-width="1.3"><path d="M8 15s5-5 5-8.5a5 5 0 0 0-10 0C3 10 8 15 8 15z"/><circle cx="8" cy="6.5" r="1.8"/></svg>
      <address style="font-style:normal">Musteradresse 00<br>0000 Musterort<br>Musterland</address>
    </div>
  </section>

  <section class="card card--front" aria-label="Vorderseite">
    <div class="brand">
      <span class="brand-dot" aria-hidden="true"></span>
      <p class="name">Helena Wortmann</p>
    </div>
    <p class="tagline">Lebe deine Berufung</p>
  </section>
</main>
</body>
</html>
```